SEO marketing site

I need a design only for an SEO/Marketing project I have in mind. I have bought the domain Brivvora.example and want to aim this project at businesses who want to push their business further. WHEN I SAY DESIGN ONLY, I MEAN NO PROGRAMMING. HOWEVER, I DO NEED THE DESIGNER TO PUT THIS SITE ONLINE. $300 IS A LOT OF MONEY FOR A TEMPLATE YOU CAN PURCHASE FOR $60 WITH SOME CUSTOMISATION.

The idea is that businesses will register with us and will be offered two different kinds of services. They can make use of our scripts to check their back links, rankings, compare with competitors and a number of other marketing tools. The other service we provide is that we offer them an SEO service at a very competitive price. We will handle social networking, link building, article submission, directory submission, social bookmarking etc etc at a reasonable monthly fee.

I qoros tram look/flat design is what I really like, and I want to give off a professional vibe. This is the kind of site I wish to go for.

JUST TO REPEAT, I NEED A DESIGN TO BE PUT ONLINE, I.E PSD TO HTML CONVERSION. MY PROGRAMMERS WILL CODE THE CLIENT AREA THEMSELVES.

Target Market(s)

Other businesses

Industry/Entity Type

Marketing

Requirements
Must have
• Qoros 8 or flat design look. Even a site, similar to makerhive, is quite attractive. I would like a killer design for the site.

```html
<!DOCTYPE html>
<html lang="en">
<head>
<meta charset="utf-8">
<title>Brivvora – Testimonials and Contact</title>
<link rel="stylesheet" href="https://fonts.googleapis.com/css2?family=Open+Sans:wght@400;600&family=Cabin:wght@400;500&display=swap">
<style>
  :root {
    --page-bg: #ffffff;
    --band-bg: #e8e8e8;
    --title-blue: #2a6ea6;
    --name-grey: #8a8a8a;
    --name-active: #2b2b2b;
    --company-light: #8ccbec;
    --company-active: #3aa0dc;
    --quote-ink: #111111;
    --footer-bg: #1f1e1e;
    --footer-top: #3a3a3a;
    --footer-head: #e9e9e9;
    --footer-text: #d6d6d6;
    --footer-muted: #8b8b8b;
    --field-bg: #ededed;
    --field-border: #7a7a7a;
    --map-bg: #9a9a9a;
    --map-border: #4a4a4a;
    --button-bg: #3a3a3a;
    --copyright: #4a4a4a;
    --icon-grey: #9a9a9a;
  }
  * { box-sizing: border-box; margin: 0; padding: 0; }
  html, body { width: 1200px; height: 900px; overflow: hidden; background: var(--page-bg); }
  body { position: relative; font-family: "Open Sans", "Verdana", sans-serif; }

  .feature-visual { position: absolute; top: 0; height: 65px; }
  .feature-visual--chart { left: 162px; width: 434px; border: 1px solid #222; border-top: none;
    background: linear-gradient(180deg, #e9edf2 0%, #f6f6f6 60%, #ffffff 100%); }
  .feature-visual--panel { left: 602px; width: 433px; background: #7f8084; }

  .testimonials { position: absolute; left: 69px; top: 120px; width: 1066px; height: 414px; background: var(--band-bg); }
  .testimonials__title { position: absolute; top: 26px; width: 100%; text-align: center;
    font-size: 28px; font-weight: 400; color: var(--title-blue); letter-spacing: 0.2px; }
  .client { position: absolute; top: 106px; width: 140px; text-align: center; }
  .client__photo { display: block; width: 100px; height: 100px; margin: 0 auto; border: 1px solid #d2d2d2; }
  .client__name { margin-top: 9px; font-size: 12px; color: var(--name-grey); line-height: 15px; }
  .client__company { font-size: 13px; color: var(--company-light); line-height: 15px; }
  .client--active .client__name { color: var(--name-active); }
  .client--active .client__company { color: var(--company-active); }
  .testimonials__quote { position: absolute; top: 286px; left: 120px; width: 826px; text-align: center;
    font-size: 16.5px; line-height: 19px; color: var(--quote-ink); }

  .site-footer { position: absolute; left: 69px; top: 534px; width: 1066px; height: 366px;
    background: linear-gradient(180deg, #2a2929 0%, var(--footer-bg) 30%, var(--footer-bg) 100%);
    border-top: 2px solid var(--footer-top); font-family: "Cabin", "Gill Sans", sans-serif; color: var(--footer-text); }
  .footer-col { position: absolute; top: 40px; }
  .footer-col__title { font-size: 13.5px; font-weight: 400; color: var(--footer-head); letter-spacing: 0.3px; margin-bottom: 11px; }
  .footer-col--categories { left: 117px; }
  .category-list { list-style: none; }
  .category-list li { font-size: 11.5px; line-height: 26.6px; }
  .footer-col--about { left: 327px; width: 180px; }
  .footer-col--about p { font-size: 11.5px; line-height: 17.7px; }
  .footer-col--contact { left: 549px; width: 420px; }
  .contact-line { font-size: 11.5px; line-height: 18.5px; }
  .contact-line span { color: var(--footer-muted); }
  .contact-details { position: absolute; top: 25px; }
  .contact-details--left { left: 0; }
  .contact-details--right { left: 212px; }
  .field { position: absolute; left: 0; width: 196px; background: linear-gradient(180deg, #f4f4f4, #e2e2e2);
    border: 1px solid var(--field-border); font-size: 10px; font-style: italic; color: #9a9a9a; padding: 1px 4px; }
  .field--name { top: 75px; height: 18px; }
  .field--email { top: 102px; height: 18px; }
  .field--message { top: 129px; height: 70px; padding-top: 3px; }
  .button { position: absolute; top: 216px; height: 18px; background: var(--button-bg); color: #eeeeee;
    font-size: 9.5px; line-height: 17px; padding-left: 4px; border-radius: 1px; box-shadow: 0 1px 0 #111; }
  .button svg { position: absolute; right: 5px; top: 4px; }
  .button--submit { left: 0; width: 58px; }
  .button--map { left: 214px; width: 72px; }
  .map-frame { position: absolute; left: 214px; top: 75px; width: 195px; height: 124px;
    background: var(--map-bg); border: 2px solid var(--map-border); }
  .copyright { position: absolute; left: 123px; top: 336px; font-size: 11px; color: var(--copyright); }
  .social-links { position: absolute; left: 836px; top: 335px; display: flex; gap: 14px; list-style: none; }
  .social-links li { width: 12px; height: 12px; background: var(--icon-grey); border-radius: 1px; }
</style>
</head>
<body>
  <div class="feature-visual feature-visual--chart" role="img" aria-label="Dashboard illustration showing reader demographics"></div>
  <div class="feature-visual feature-visual--panel" role="img" aria-label="Feature slide image"></div>

  <section class="testimonials">
    <h2 class="testimonials__title">What people are saying about us</h2>

    <div class="client" style="left:124px">
      <span class="client__photo" role="img" aria-label="Portrait photo of Marit Solberg" style="background:linear-gradient(160deg,#dcdcdc,#b89a86)"></span>
      <p class="client__name">Marit Solberg</p><p class="client__company">Kelvix</p>
    </div>
    <div class="client" style="left:295px">
      <span class="client__photo" role="img" aria-label="Portrait photo of Anton Reyes" style="background:linear-gradient(160deg,#8e8e8e,#c9c9c9)"></span>
      <p class="client__name">Anton Reyes</p><p class="client__company">Orvana</p>
    </div>
    <div class="client" style="left:464px">
      <span class="client__photo" role="img" aria-label="Portrait photo of Lena Marsh" style="background:linear-gradient(160deg,#f0f0f0,#e2cfc0)"></span>
      <p class="client__name">Lena Marsh</p><p class="client__company">Fenlow</p>
    </div>
    <div class="client client--active" style="left:635px">
      <span class="client__photo" role="img" aria-label="Portrait photo of Dorian Pike" style="background:linear-gradient(160deg,#e6e6e6,#7b5d4d 60%,#3c6fa8)"></span>
      <p class="client__name">Dorian Pike</p><p class="client__company">Tridel</p>
    </div>
    <div class="client" style="left:805px">
      <span class="client__photo" role="img" aria-label="Portrait photo of Tomas Wren" style="background:linear-gradient(160deg,#9fc6e6,#caa68e 60%,#6a6f78)"></span>
      <p class="client__name">Tomas Wren</p><p class="client__company">Zestra</p>
    </div>

    <p class="testimonials__quote">“If you are getting a lot of requests for advertising on your site, and feel bogged down managing it all yourself, I would definitely recommend giving Brivvora a try. ”</p>
  </section>

  <footer class="site-footer">
    <div class="footer-col footer-col--categories">
      <h3 class="footer-col__title">BROWSE CATAGORIES</h3>
      <ul class="category-list">
        <li>Lorem ipsum dolor sit amet.</li>
        <li>Lorem ipsum dolor sit amet.</li>
        <li>Lorem ipsum dolor sit amet.</li>
        <li>Lorem ipsum dolor sit amet.</li>
        <li>Lorem ipsum dolor sit amet.</li>
      </ul>
    </div>

    <div class="footer-col footer-col--about">
      <h3 class="footer-col__title">ABOUT US</h3>
      <p>Lorem ipsum dolor sit amet, consectetur adipiscing elit. Duis mattis varius ultricies. Donec quam odio, tincidunt at iaculis nec, vulputate eu nibh. In arcu purus, auctor at fringilla id, ves­tibulum nec turpis. Maecenas convallis nisi elit, eu sodales nisl egestas quis. Nullam mattis, dui quis vestibulum tempor, lacerat nibh lectus, vel imperdiet massa posuere non. Pellentesque pulvinar feugiat justo, cursus</p>
    </div>

    <div class="footer-col footer-col--contact">
      <h3 class="footer-col__title">CONTACT US</h3>
      <div class="contact-details contact-details--left">
        <p class="contact-line"><span>Adress:</span> Norland,Vesterhaven, Linde 12</p>
        <p class="contact-line"><span>E-mail:</span> info@brivvora.example</p>
      </div>
      <div class="contact-details contact-details--right">
        <p class="contact-line"><span>Tel.:</span> +00 555 010 2304</p>
        <p class="contact-line"><span>Fax.:</span> +00 555 010 2534</p>
      </div>

      <div class="field field--name">Your name</div>
      <div class="field field--email">E-mail</div>
      <div class="field field--message">Message</div>
      <div class="button button--submit">Submit
        <svg width="11" height="8" viewBox="0 0 11 8"><rect x="0.5" y="0.5" width="10" height="7" fill="none" stroke="#ddd"/><path d="M0.5 0.5 L5.5 4.5 L10.5 0.5" fill="none" stroke="#ddd"/></svg>
      </div>

      <div class="map-frame" role="img" aria-label="Location map with office marker"></div>
      <div class="button button--map">Bigger map
        <svg width="8" height="8" viewBox="0 0 8 8"><circle cx="4" cy="4" r="3" fill="none" stroke="#ddd"/><path d="M4 2 V6 M2 4 H6" stroke="#ddd"/></svg>
      </div>
    </div>

    <p class="copyright">© Copyright 2013 Brivvora</p>
    <ul class="social-links" aria-label="Social links">
      <li aria-label="Feed"></li>
      <li aria-label="Social network one"></li>
      <li aria-label="Social network two"></li>
      <li aria-label="Social network three"></li>
      <li aria-label="Photo sharing"></li>
    </ul>
  </footer>
</body>
</html>
```